Kiddies Tinker Harbour

We are a company that is going to offer birthday party hire of construction toys for boys to learn to develop their skills, e.g.: brikko, blocks, building supplies etc. We are also in the process of setting up an onsite location for birthday parties, where the kids can be entertained by the equipment and the parents can have a coffee and relax during the week and birthday parties during the weekend. We do require a booking system where people can book - it needs to take the booking and then we will email them out a confirmation with payment details on it and they can pay directly into our bank account.

Industry/Entity Type

Construction

Number of Pages Required

5+ page

Font styles to use
Sans Serif

Requirements
Should not have
• No mention of Building Bricks brand, use building bricks instead

```html
<!DOCTYPE html>
<html lang="en">
<head>
<meta charset="utf-8">
<title>Kiddies Tinker Harbour</title>
<link href="https://fonts.googleapis.com/css2?family=Open+Sans:wght@400;600&family=Raleway:wght@400;500;700;800&display=swap" rel="stylesheet">
<style>
:root{
  --sky-top:#3a9be0;
  --sky-mid:#8cc8ef;
  --white:#ffffff;
  --nav:#1f86d1;
  --nav-dark:#1670b3;
  --red:#e2312f;
  --yellow:#ffe000;
  --blue:#1b8ad3;
  --light-blue:#4db8e8;
  --green:#8dbf2e;
  --green-foot:#78c043;
  --green-dark:#5aa72d;
  --text:#555555;
  --muted:#8a8a8a;
}
*{box-sizing:border-box;margin:0;padding:0}
html,body{width:790px;height:1200px;overflow:hidden}
body{position:relative;font-family:"Open Sans",sans-serif;color:var(--text);background:var(--white)}
.sky{position:absolute;left:0;top:0;width:790px;height:800px;background:linear-gradient(180deg,var(--sky-top) 0%,var(--sky-mid) 18%,#e6f3fb 34%,var(--white) 46%)}
.brand{position:absolute;left:0;width:790px;top:48px;text-align:center;font-family:"Raleway",sans-serif;font-weight:800;font-size:20px;color:var(--white);display:flex;justify-content:center;align-items:center;gap:8px}
.brand .dot{width:18px;height:18px;border-radius:50%;background:var(--yellow)}
.call{position:absolute;left:560px;top:59px;width:103px;text-align:right;color:#222;font-size:8px;font-weight:400}
.call strong{display:flex;justify-content:flex-end;align-items:center;gap:3px;font-family:"Raleway",sans-serif;font-weight:500;font-size:13px;color:var(--white)}
.nav{position:absolute;left:129px;top:94px;width:533px;height:32px;background:linear-gradient(180deg,#2c95dc,var(--nav-dark));display:flex}
.nav a{color:var(--white);text-decoration:none;font-family:"Raleway",sans-serif;font-weight:500;font-size:10px;display:flex;align-items:center;justify-content:center;border-right:1px solid rgba(255,255,255,.35);flex:auto}
.nav a:last-child{border-right:none}
.hero{position:absolute;left:129px;top:126px;width:533px;height:240px;background:linear-gradient(120deg,#cfc9c3 0%,#e4ddd5 40%,#b9b2ab 100%)}
.hero-dots{position:absolute;left:372px;top:348px;display:flex;gap:3px}
.hero-dots span{width:10px;height:10px;border-radius:50%;background:var(--white)}
.booking{position:absolute;left:479px;top:149px;width:160px;height:181px;background:var(--red);border:2px solid #f4b7b3;border-radius:9px;padding:20px 17px 0}
.booking h2{font-family:"Raleway",sans-serif;font-weight:500;font-size:16px;color:var(--white);text-align:center}
.booking p{font-size:6px;color:var(--white);text-align:center;margin:2px 0 10px}
.booking .field{height:15px;background:var(--white);border:1px solid #ddd;margin-bottom:4px;font-size:5.5px;color:#999;padding:4px 5px}
.booking .btn{height:21px;background:var(--yellow);font-family:"Raleway",sans-serif;font-weight:700;font-size:8px;color:#222;display:flex;align-items:center;justify-content:center;margin-top:7px}
.section-title{position:absolute;left:0;width:790px;top:387px;text-align:center;font-family:"Raleway",sans-serif;font-weight:400;font-size:14px;color:#333}
.product{position:absolute;top:421px;width:120px;height:120px;border-radius:50%;overflow:hidden;border:3px solid var(--white);box-shadow:0 2px 6px rgba(0,0,0,.3);background:linear-gradient(160deg,#f2eee8,#d9d2c8)}
.product .band{position:absolute;left:0;bottom:0;width:100%;height:44px;border-radius:60% 60% 0 0/30% 30% 0 0;display:flex;align-items:center;justify-content:center;text-align:center;color:var(--white);font-family:"Raleway",sans-serif;font-weight:500;font-size:11px;line-height:1}
.product .band small{display:block;font-size:8px;margin-top:1px}
.about h1{position:absolute;left:130px;top:598px;font-family:"Raleway",sans-serif;font-weight:400;font-size:19px;color:var(--blue)}
.about p{position:absolute;left:130px;width:262px;font-size:6.6px;line-height:11.5px;color:var(--muted)}
.btn-green{position:absolute;left:131px;top:716px;width:75px;height:21px;background:linear-gradient(180deg,#9fca43,#7aa82a);color:var(--white);font-family:"Raleway",sans-serif;font-size:8.5px;display:flex;align-items:center;justify-content:center}
.about-photo{position:absolute;left:398px;top:558px;width:274px;height:202px;background:linear-gradient(135deg,#f4f4f4 0%,#d8e6d0 40%,#e8d86a 70%,#f4f4f4 100%);border-radius:4px}
.divider{position:absolute;left:60px;top:770px;width:670px;height:22px;background:radial-gradient(ellipse at top,rgba(0,0,0,.08),transparent 70%)}
.playground{position:absolute;left:0;top:870px;width:790px;height:152px;background:linear-gradient(180deg,rgba(220,220,220,0),#e4e4e4 45%,#dcdcdc)}
.card{position:absolute;top:808px;width:171px;height:176px;background:var(--white);border:1px solid #e2e2e2;text-align:center}
.card .photo{height:82px}
.card h3{font-family:"Raleway",sans-serif;font-weight:500;font-size:11px;color:#333;margin:10px 0 5px}
.card p{font-size:5.6px;line-height:11px;color:var(--muted);padding:0 10px}
.card .btn{display:inline-flex;width:62px;height:17px;margin-top:7px;align-items:center;justify-content:center;color:var(--white);font-size:7px;border-radius:2px}
.footer{position:absolute;left:0;top:1022px;width:790px;height:146px;background:linear-gradient(180deg,#8cce52,var(--green-foot))}
.footer .col{position:absolute;top:26px}
.footer h4{font-family:"Raleway",sans-serif;font-weight:500;font-size:10px;color:var(--white);margin-bottom:6px}
.footer li{list-style:none;font-size:7.6px;line-height:16.8px;color:var(--white)}
.social{display:flex;gap:4px;margin-top:3px}
.social span{width:20px;height:20px;border-radius:50%;background:#3a7fd0;border:2px solid var(--white)}
.copy{position:absolute;left:0;top:1168px;width:790px;height:32px;background:var(--green-dark);color:#e9f5dc;font-size:6.5px;padding:12px 0 0 128px}
</style>
</head>
<body>
<div class="sky"></div>

<header>
  <div class="brand"><span class="dot"></span>Kiddies Tinker Harbour</div>
  <div class="call">Call Us Now
    <strong><svg width="10" height="10" viewBox="0 0 24 24"><path fill="#fff" d="M6.6 10.8a15.1 15.1 0 0 0 6.6 6.6l2.2-2.2a1 1 0 0 1 1-.25 11.4 11.4 0 0 0 3.6.57 1 1 0 0 1 1 1V20a1 1 0 0 1-1 1A17 17 0 0 1 3 4a1 1 0 0 1 1-1h3.5a1 1 0 0 1 1 1c0 1.250.2 2.450.57 3.57a1 1 0 0 1-.25 1z"/></svg>555.214.7730</strong>
  </div>
  <nav class="nav">
    <a>WHY US</a><a>PRODUCTS</a><a>SERVICES</a><a>PROJECTS</a><a>BLOG</a><a>ONLINE SHOP</a><a>CONTACT US</a>
  </nav>
</header>

<section>
  <div class="hero" role="img" aria-label="Photo of a young girl building a tall tower of colourful bricks"></div>
  <form class="booking">
    <h2>BOOKING NOW</h2>
    <p>MAECENAS ALIQUET VELIT VEL</p>
    <div class="field">Your Name</div>
    <div class="field">Email address</div>
    <div class="field">Toys u want to book</div>
    <div class="field">Location</div>
    <div class="btn">BOOK NOW</div>
  </form>
  <div class="hero-dots"><span></span><span></span><span></span></div>
</section>

<section>
  <h2 class="section-title">Product We Provides</h2>
  <div class="product" style="left:135px" role="img" aria-label="Photo of red and blue building bricks"><div class="band" style="background:var(--red)"><div>Building<small>Bricks</small></div></div></div>
  <div class="product" style="left:270px" role="img" aria-label="Photo of a small building made of blocks"><div class="band" style="background:var(--light-blue)"><div>Building<small>Supplies</small></div></div></div>
  <div class="product" style="left:406px" role="img" aria-label="Photo of a tray full of loose blocks"><div class="band" style="background:var(--green)">Blocks</div></div>
  <div class="product" style="left:541px" role="img" aria-label="Photo of toy construction trucks"><div class="band" style="background:var(--blue)">Trucks &amp; Rail</div></div>
</section>

<section class="about">
  <h1>Kiddies Tinker Harbour</h1>
  <p style="top:630px">Donec quis mi sed magna hendrerit accumsan Suspendisse risus nibh ultricies eu volutpat non condimentum hendrerit augue Etiam eleifend metus</p>
  <p style="top:657px">Maecenas aliquet velit vel turpis Mauris neque metus malesuada nec ultricies sit amet porttitor mattis enim In massa libero interdum nec interdum vel blandit sed nulla In ullamcorper est eget tempor cursus neque mi consectetuer mi a ultricies massa est sed nisl Class aptent taciti sociosqu ad litora torquent per</p>
  <div class="btn-green">Read More</div>
  <div class="about-photo" role="img" aria-label="Photo of a toddler stacking large coloured bricks into a wall"></div>
  <div class="divider"></div>
</section>

<section>
  <div class="playground" role="img" aria-label="Faint playground silhouette"></div>
  <article class="card" style="left:128px">
    <div class="photo" role="img" aria-label="Photo of a child playing among colourful bricks" style="background:linear-gradient(135deg,#f3a6c6,#f6d34a,#5ab6e8)"></div>
    <h3>How Construction Kids Help</h3>
    <p>dum nec interdum vel blandit sed nulla In ullam corper est eget tempor cursus neque mi consectetuer mi a ultricies massa</p>
    <span class="btn" style="background:var(--light-blue)">Read More</span>
  </article>
  <article class="card" style="left:309px">
    <div class="photo" role="img" aria-label="Photo of a smiling parent and child" style="background:linear-gradient(135deg,#e9c7a2,#c98e6a,#f2dcc5)"></div>
    <h3>What Parents Says</h3>
    <p>dum nec interdum vel blandit sed nulla In ullam corper est eget tempor cursus neque mi consectetuer mi a ultricies massa</p>
    <span class="btn" style="background:var(--red)">Read More</span>
  </article>
  <article class="card" style="left:490px">
    <div class="photo" role="img" aria-label="Photo of a toddler next to brick towers" style="background:linear-gradient(135deg,#3fa3e0,#f0e4d0,#e4392f)"></div>
    <h3>Develop Kids Skill</h3>
    <p>dum nec interdum vel blandit sed nulla In ullam corper est eget tempor cursus neque mi consectetuer mi a ultricies massa</p>
    <span class="btn" style="background:var(--nav-dark)">Read More</span>
  </article>
</section>

<footer class="footer">
  <div class="col" style="left:131px"><h4>QUICK LINKS</h4><ul><li>Why Choose Us</li><li>Our Products</li><li>Bookign Now</li><li>What Parents says</li></ul></div>
  <div class="col" style="left:248px"><h4>RESOURCES</h4><ul><li>Blog</li><li>Prices</li><li>Contact Us</li></ul></div>
  <div class="col" style="left:355px"><h4>CONTACT INFO</h4><ul><li>42 Harbour Lane #B</li><li>Brookvale 20415 BV</li><li>Phone: 555.214.7731</li><li>Email: hello@kiddiestinker.com</li></ul></div>
  <div class="col" style="left:509px"><h4>STAY IN TOUCH</h4><div class="social"><span></span><span></span><span></span><span></span><span></span></div></div>
</footer>
<div class="copy">© 2015 Company Name &nbsp;All right reserved &nbsp;Term of Use</div>
</body>
</html>
```